Professional and stylish textiles catalogue

Wool throws and cushions product catalogue.
Target audience are business customers (interior stores). Besides providing information about products the catalogue must able to sell, therefore we expect it to be professional and stylish.
Size A5 horizontal.
Content:
1. Cover: Logo and 2011/12 on front, company details on reverse;
2. Page with photo and short info about company;
3. Product pages spread - one item per page. Total 15 double-page spreads;
4. Info page with photo and small text about gift packaging.
Products - throws and cushions. Located as a pair on each spread: throw on the left, cushion on the right. One double-page spread with three throws.
Products mostly are in natural colours: grey, beige and brown. Three throws/cushions in light shades of rose, green and blue.
Comments: catalogue must be in bright colours, could be white with colourful details. Will be great if each product's double-page spread will have stylish details (could be lines) in colours of the product located in this certain double-page spread.
Materials provided:
1. Texts;
2. White background pictures of each product;
3. Several product pictures taken in the interior to use for the cover;
4. Logo.
Complete set of pictures in high resolution will be provided on request.

```html
<!DOCTYPE html>
<html lang="en">
<head>
<meta charset="utf-8">
<title>Lanvere 2011/12 Range – Catalogue Pages</title>
<link rel="stylesheet" href="https://fonts.googleapis.com/css2?family=Marcellus&display=swap">
<style>
  :root {
    --backdrop: #d9edf9;
    --paper: #ffffff;
    --slate: #474b58;
    --taupe: #b4a7a1;
    --ink: #5f5f63;
    --ink-soft: #7b7b80;
    --rule: #c9c9cc;
    --rule-dark: #6c707c;
    --on-slate: #e6e7ea;
    --photo-a: #d9d3cb;
    --photo-b: #a9a49c;
    --throw-a: #e9e4dd;
    --throw-b: #c4bab1;
    --rose-a: #d9c6c1;
    --rose-b: #a58c86;
  }
  * { box-sizing: border-box; margin: 0; padding: 0; }
  html, body { width: 1080px; height: 1200px; overflow: hidden; }
  body {
    background: var(--backdrop);
    font-family: "Marcellus", "Optima", serif;
    color: var(--ink);
    position: relative;
  }
  .page, .spread {
    position: absolute;
    background: var(--paper);
    box-shadow: 0 1px 4px rgba(40, 60, 80, .25);
    overflow: hidden;
  }
  .rule { position: absolute; height: 1px; background: var(--rule); }
  .mark { position: absolute; width: 10px; height: 10px; background: var(--ink); }
  .photo { position: absolute; }

  /* Cover */
  .cover { left: 537px; top: 33px; width: 506px; height: 356px; }
  .brand {
    position: absolute; right: 36px; top: 28px;
    font-size: 32px; letter-spacing: 1px; color: var(--ink);
    display: flex; align-items: center; gap: 12px;
  }
  .brand::before { content: ""; width: 22px; height: 22px; background: var(--ink); }
  .cover .photo {
    left: 0; top: 70px; width: 469px; height: 225px;
    background: linear-gradient(100deg, var(--photo-b) 0%, var(--photo-a) 45%, #f1eee9 70%, var(--photo-b) 100%);
  }
  .range {
    position: absolute; right: 36px; top: 302px;
    font-size: 19px; letter-spacing: 1px; color: var(--ink-soft);
  }

  /* About spread */
  .about { left: 33px; top: 421px; width: 1010px; height: 356px; }
  .about .intro-page {
    position: absolute; left: 0; top: 0; width: 504px; height: 100%;
    background: var(--slate);
  }
  .intro-page .rule { background: var(--rule-dark); left: 38px; width: 430px; }
  .intro {
    position: absolute; left: 0; top: 100px; width: 504px;
    text-align: center; font-size: 17px; line-height: 25.5px; color: var(--on-slate);
  }
  .about .text-page { position: absolute; left: 504px; top: 0; width: 506px; height: 100%; }
  .text-page .rule { left: 36px; width: 428px; }
  .text-page .photo { left: 66px; top: 8px; width: 420px; height: 255px; }
  .values {
    position: absolute; left: 36px; top: 52px; width: 185px;
    font-size: 11px; line-height: 14.6px; color: var(--ink);
  }
  .collection {
    position: absolute; left: 36px; top: 246px; width: 330px;
    font-size: 11px; line-height: 14.6px; color: var(--ink);
  }
  .text-page .mark { right: 20px; top: 326px; }

  /* Product spread */
  .product { left: 36px; top: 811px; width: 1007px; height: 358px; }
  .band { position: absolute; top: 0; height: 100%; background: var(--taupe); }
  .band.left { left: 0; width: 13px; }
  .band.gutter { left: 469px; width: 71px; }
  .band.right { right: 0; width: 9px; }
  .product .rule.top-l { left: 35px; width: 434px; top: 37px; }
  .product .rule.top-r { left: 540px; width: 433px; top: 37px; }
  .product .rule.bot-l { left: 35px; width: 434px; top: 320px; }
  .product .rule.bot-r { left: 540px; width: 433px; top: 320px; }
  .product .art { position: absolute; left: 0; top: 0; }
  .item-title { position: absolute; top: 29px; }
  .item-title h2 {
    font-weight: 400; font-size: 14px; letter-spacing: .4px; color: var(--ink);
    background: var(--paper); display: inline-block; padding: 0 6px 0 0;
  }
  .item-title p { font-size: 11.5px; color: var(--ink); margin-top: 1px; }
  .item-title .specs { font-size: 8.5px; line-height: 12px; color: var(--ink-soft); margin-top: 10px; }
  .item-left { left: 35px; }
  .item-right { right: 34px; text-align: right; }
  .item-right h2 { padding: 0 0 0 6px; }
  .style-no { position: absolute; top: 254px; font-size: 8px; color: var(--ink-soft); display: flex; align-items: center; gap: 3px; }
  .style-no.left { left: 313px; }
  .style-no.right { left: 622px; }
  .product .mark { right: 21px; top: 325px; }
</style>
</head>
<body>

  <section class="page cover">
    <div class="brand">LANVERE</div>
    <div class="photo" role="img" aria-label="Cream fringed throw draped over the arm of a grey upholstered chair"></div>
    <div class="range">2011/12 RANGE</div>
  </section>

  <section class="spread about">
    <div class="intro-page">
      <div class="rule" style="top:35px"></div>
      <p class="intro">Lanvere is a textile design company<br>established in London in 2010<br>with the intention of creating high quality,<br>environmentally friendly, handwoven<br>throws and cushions.</p>
      <div class="rule" style="top:320px"></div>
    </div>
    <div class="text-page">
      <div class="rule" style="top:35px"></div>
      <svg class="photo" role="img" aria-label="Rolled brown and pink patterned alpaca throw with fringe" viewBox="0 0 420 255" width="420" height="255">
        <defs>
          <linearGradient id="rose" x1="0" y1="1" x2="1" y2="0">
            <stop offset="0" stop-color="var(--rose-a)"/>
            <stop offset="1" stop-color="var(--rose-b)"/>
          </linearGradient>
        </defs>
        <polygon points="130,190 250,70 380,30 410,60 400,200 230,250 150,235" fill="url(#rose)"/>
      </svg>
      <p class="values">Values like beauty, long-lasting quality and harmony with nature, humans and objects lead to the creation of Lanvere accessories which are in classic designs, made with the environment in mind and sourced from sustainable materials.</p>
      <p class="collection">The 2011/12 collection<br>is made from finest Peruvian baby alpaca,<br>utilizing ancient Andean textile expertise and woven on traditional handlooms by professional handweavers in Peru.</p>
      <div class="rule" style="top:320px"></div>
      <div class="mark"></div>
    </div>
  </section>

  <section class="spread product">
    <div class="band left"></div>
    <div class="band gutter"></div>
    <div class="band right"></div>
    <div class="rule top-l"></div>
    <div class="rule top-r"></div>

    <svg class="art" viewBox="0 0 1007 358" width="1007" height="358" aria-hidden="false">
      <defs>
        <linearGradient id="wool" x1="0" y1="0" x2="1" y2="1">
          <stop offset="0" stop-color="var(--throw-a)"/>
          <stop offset="1" stop-color="var(--throw-b)"/>
        </linearGradient>
      </defs>
      <polygon role="img" aria-label="Beige checked handwoven alpaca throw with fringed edge"
               points="277,12 411,139 404,256 151,339 77,216 197,109" fill="url(#wool)"/>
      <polygon role="img" aria-label="Beige checked handwoven alpaca cushion"
               points="764,14 941,183 777,347 611,183" fill="url(#wool)"/>
    </svg>

    <div class="item-title item-left">
      <h2>HIGHLAND CHECK</h2>
      <p>Handwoven Throw</p>
      <p class="specs">100% baby alpaca<br>Natural, undyed colours<br>Size 127 x 175 cm</p>
    </div>
    <div class="style-no left">
      <svg width="9" height="7" viewBox="0 0 9 7"><polygon points="9,0 9,7 0,3.5" fill="#7b7b80"/></svg>Style nr. 0100501
    </div>

    <div class="item-title item-right">
      <h2>HIGHLAND CHECK</h2>
      <p>Handwoven Cushion</p>
      <p class="specs">100% baby alpaca<br>Natural, undyed colours<br>Size 50 x 50 cm</p>
    </div>
    <div class="style-no right">Style nr. 020050
      <svg width="9" height="7" viewBox="0 0 9 7"><polygon points="0,0 0,7 9,3.5" fill="#7b7b80"/></svg>
    </div>

    <div class="rule bot-l"></div>
    <div class="rule bot-r"></div>
    <div class="mark"></div>
  </section>

</body>
</html>
```